Website development company website

ABOUT COMPANY
Hi everyone! We're a Melbourne, Australia website development company in a need of a website design that will make online store merchants want to engage our services.
We specialise exclusively in Vendrik e-commerce platform (https://vendrik.example/). What distinguishes our business from competition is that rather than designing and building brand new websites, we offer development, support and maintenance services to established websites. Maintenance and Support are the keywords representing our business.
Our potential clients are people with broken, slow and underperforming Vendrik installations who need assistance getting their websites up and making sales. Our website must pass the message that we can help, and provide quick means of making contact.
DESIGN
Overall, we're looking for a slick, clean, airy, conservative design. No need to do anything crazy, try to stick to what's "standard" in website design these days and make it easy on all of us. The website is unlikely to be updated too often so it needs to look attractive and fresh first time over and after a year, too.
Attached is our new logo, which you'll be able to take the basic idea from, the colors and fonts. Though, don't use the fonts from the logo in the website, stick to the standard widely supported fonts. Additional use of Plinth fonts is fine.
Don't overdo it with colors, stick to conservative basic color set and only use the colors from the log for accents like headings etc. Please, don't be tempted to use the blue and orange as background of whole blocks, other than perhaps footer. Thanks.
For the images used, I'd like to stay away from a design studio/digital agency feel and lean more towards professional support and maintenance services. I'm thinking images of content merchants doing their job. Something along the lines of "We'll be taking care of the website so that you only need to care about the business".
Some ideas I like:
http://www.pixbarrow.example/detail/photo/portrait-of-confident-male-design-professional-royalty-free-image/520947381
http://www.pixbarrow.example/detail/photo/designer-taking-picture-of-hat-high-res-stock-photography/738205164
http://www.pixbarrow.example/detail/photo/woman-packaging-pottery-royalty-free-image/216483905
Images of colorful shopping bags and shopping carts are over the top and not serious enough. Instead of images matching Online Shopping, I'd try going more for Stability, Reliability, Performance.
Our existing website is http://www.tralvo.example. Please, don't take design ideas from it, but it will give you a picture of the structure of our new website and content that's going to be used initially.
If you could include a basic icon set to use throughout the website, that would be great. If the icons could match our logo (attached), it would be a big plus.
ALL PAGES
Every page must contain clearly visible phone number (1300 648 507) and a Contact Us Now button, which opens an AJAX driven popup form with Name, Email, Phone and Message to be sent through.
To start with, main menu items will be Vendrik, Portfolio, Contact.
At the bottom of each page, please, include a newsletter subscription form with text Subscribe to Vendrik Support and Security Updates.
For the footer, I'd like to see a logo strip with the following logos in grayscale (no need to link anywhere): Vendrik, QRX, DataNest, KLV. You'll find the logos on Plinth Pictures.
Standard footer columns follow. Here, I'd like to see logos in color: Vendrik Certified Developer, Vendrik Ceritified Solution Provider. Again, the logos are on Plinth Pictures.
No social media logos/links necessary anywhere on the website.
...and then the copyright line.
FRONT PAGE
Large slider with images that would appeal to our target audience. Keywords here would be Vendrik System Audit, Vendrik Performance Optimisation, Vendrik Website Emergency Recovery, Vendrik Development Infrastructure Hosting. We'll have a static page created for each of these to link to.
In a corner of the slider, or on the edge, can I have an overlay with logos in color (same as footer): Vendrik Certified Developer, Vendrik Ceritified Solution Provider.
Underneath, a number of blocks, each with an image and teaser that we'll use to link to various pages throughout the website.
PORTFOLIO PAGE
I'm thinking a single long page with a block per client, which will contain project name, description from us and a testimonial from client. Also, each block will contain a single large screenshot. No gallery or slideshow is necessary here, just one image per project.
I'll leave the layout up to you, but try to put yourself in the shoes of a potential client reviewing our past work by simply scrolling down this one page.
CONTACT US PAGE
Separate page with the same form as above, phone number (1300 648 507), email address (support@mibrel.example), address (Suite 42, Level 3|8 Harlow Bend Road|Wendale Flats VIC 3921), and a grayscale Plinth Chart.
CODING UP
Coding up into static HTML/CSS/JS is equally important as the design itself. We're a website development company, we'll be integrating the theme. We will spot any issues and we will point them out.
Coded up design must be fully responsive. Enough said.
To be able to create any content in future, we'd like one extra page coded up with samples of all themed elements, lists, forms, buttons, 2, 3, 4-column layout, alerts, icons, etc. This page does not need to be designed, only coded up.
The design will be integrated into Drupal using Twig. If possible at all, try to keep it in mind when designing and coding up, and make the integration into a Drupal theme easier for us.
GOOD LUCK!
That's it. Let me know if anything needs clarifying. So far I've had a great experience with ArtHarbor. I don't doubt some great designs will emerge. Clever ideas are highly appreciated, but also make it clear you've read and followed the points in this brief. Cheers, Kip

```html
<!DOCTYPE html>
<html lang="en">
<head>
<meta charset="utf-8">
<title>Halvert Commerce – Vendrik Support &amp; Maintenance</title>
<link href="https://fonts.googleapis.com/css2?family=Roboto:wght@300;400;500&display=swap" rel="stylesheet">
<style>
:root{
  --orange:#e8822a;
  --navy:#1d3a6b;
  --ink:#3c3c3c;
  --muted:#777;
  --line:#d6d6d6;
  --panel:#f2f2f2;
  --band:#ebebeb;
  --dark:#3a3a3a;
  --white:#fff;
}
*{box-sizing:border-box;margin:0;padding:0}
html,body{width:734px;height:1200px;overflow:hidden}
body{font-family:"Roboto",Arial,sans-serif;color:var(--ink);background:var(--white);position:relative}
a{text-decoration:none;color:inherit}

.site-header{position:absolute;left:0;top:0;width:734px;height:76px;background:var(--white)}
.brand{position:absolute;left:62px;top:26px;display:flex;align-items:center;gap:6px}
.brand__mark{width:22px;height:22px;background:var(--navy)}
.brand__name{font-size:19px;font-weight:500;color:var(--navy);line-height:1}
.call-line{position:absolute;right:62px;top:12px;font-size:7px;color:var(--muted)}
.call-line strong{font-size:9px;font-weight:400;color:var(--orange);margin-left:4px}
.main-nav{position:absolute;left:391px;top:37px;display:flex;align-items:center}
.main-nav a{font-size:7.5px;color:var(--ink);margin-right:38px;text-transform:uppercase}
.main-nav a.is-active{background:var(--orange);color:var(--white);width:54px;height:24px;line-height:24px;text-align:center;border-radius:3px;margin-right:24px}

.hero{position:absolute;left:0;top:76px;width:734px;height:375px;
  background:
    radial-gradient(ellipse 150px 110px at 440px 235px,rgba(150,70,70,.45),rgba(150,70,70,0) 70%),
    radial-gradient(ellipse 210px 150px at 560px 140px,rgba(110,118,126,.55),rgba(110,118,126,0) 75%),
    radial-gradient(ellipse 170px 140px at 300px 190px,rgba(215,205,195,.55),rgba(215,205,195,0) 70%),
    radial-gradient(ellipse 220px 200px at 110px 250px,rgba(140,140,138,.75),rgba(140,140,138,0) 75%),
    linear-gradient(160deg,#55574f 0%,#3a3c38 30%,#2b3036 55%,#30353b 80%,#44484c 100%)}
.hero__controls{position:absolute;left:62px;top:342px;display:flex;gap:2px}
.hero__arrow{width:22px;height:22px;background:rgba(60,60,60,.85);display:flex;align-items:center;justify-content:center}
.hero__badges{position:absolute;left:558px;top:298px;display:flex;gap:20px;align-items:flex-end}
.badge-plain{width:48px;height:48px;background:var(--orange);border-radius:4px}
.badge-cert{width:38px;height:66px;background:#bfc2c4;border-radius:3px}

.services{position:absolute;left:0;top:451px;width:734px;height:254px;background:var(--panel)}
.service-card{position:absolute;top:63px;width:148px;height:162px;background:var(--white);border:1px solid var(--line);text-align:center}
.service-card__icon{position:absolute;left:50%;top:-33px;transform:translateX(-50%);width:64px;height:64px;border-radius:50%;background:var(--dark);border:4px solid #e6e6e6;display:flex;align-items:center;justify-content:center}
.service-card__icon--accent{background:var(--orange)}
.service-card__title{margin-top:42px;font-size:10.5px;font-weight:400;color:var(--navy);line-height:16px;padding:0 14px}
.service-card__text{margin-top:12px;font-size:6.6px;line-height:11.5px;color:var(--muted);font-weight:300;padding:0 7px}
.btn-outline{display:inline-block;margin-top:12px;height:21px;line-height:19px;padding:0 7px;border:1px solid #555;border-radius:4px;font-size:7px;color:var(--ink)}
.btn-outline--accent{border-color:var(--orange);color:var(--orange)}

.intro-cols{position:absolute;left:0;top:705px;width:734px;height:184px}
.intro-col{position:absolute;top:22px;width:178px}
.intro-col h2{font-size:20px;font-weight:300;line-height:26px;color:var(--ink)}
.intro-col p{margin-top:16px;font-size:6.8px;line-height:12.6px;color:var(--muted);font-weight:300;text-align:justify}
.intro-col .text-link{position:absolute;top:138px;left:1px;font-size:7px;color:var(--orange);text-decoration:underline}

.cert-band{position:absolute;left:0;top:889px;width:734px;height:154px;background:var(--band)}
.cert-band__badge{position:absolute;left:115px;top:16px;width:73px;height:123px;background:linear-gradient(#cfd1d2,#9b9ea0);border-radius:4px}
.cert-band h3{position:absolute;left:265px;top:22px;font-size:10px;font-weight:500;color:var(--ink);letter-spacing:.2px}
.cert-band p{position:absolute;left:265px;top:41px;width:408px;font-size:7px;line-height:12.6px;color:var(--muted);font-weight:300;text-align:justify}

.site-footer{position:absolute;left:0;top:1043px;width:734px;height:152px;background:var(--white)}
.footer-brand{position:absolute;left:60px;top:52px;display:flex;align-items:center;gap:6px}
.footer-brand__mark{width:22px;height:22px;background:#9a9a9a}
.footer-brand__name{font-size:17px;font-weight:500;color:#8a8a8a}
.footer-address{position:absolute;left:189px;top:26px;font-size:7.2px;line-height:12.6px;color:var(--ink)}
.footer-address h4{font-size:11.5px;font-weight:400;margin-bottom:10px}
.footer-address p{margin-bottom:9px}
.tech-strip{position:absolute;left:322px;top:40px;width:160px;display:grid;grid-template-columns:1fr 1fr;row-gap:26px;column-gap:14px}
.tech-strip span{font-size:13px;font-weight:500;color:#b5b5b5;text-align:center}
.footer-map{position:absolute;left:503px;top:27px;width:170px;height:100px;background:linear-gradient(135deg,#e2e2e2,#cacaca);border:1px solid #999}
.footer-rule{position:absolute;left:0;top:1195px;width:734px;height:5px;background:#9a9a9a}
</style>
</head>
<body>
<header class="site-header">
  <a class="brand" href="#"><span class="brand__mark"></span><span class="brand__name">Halvert</span></a>
  <div class="call-line">Call now for more information <strong>1300 648 507</strong></div>
  <nav class="main-nav">
    <a class="is-active" href="#">Home</a>
    <a href="#">About Us</a>
    <a href="#">Portfolio</a>
    <a href="#" style="margin-right:0">Contact Us</a>
  </nav>
</header>

<section class="hero" role="img" aria-label="Slider photo: a hand in a grey sweater tapping the add to cart button of an online shop on a tablet">
  <div class="hero__controls">
    <span class="hero__arrow"><svg width="8" height="12" viewBox="0 0 8 12"><path d="M7 1L2 6l5 5" fill="none" stroke="#ccc" stroke-width="1.4"/></svg></span>
    <span class="hero__arrow"><svg width="8" height="12" viewBox="0 0 8 12"><path d="M1 1l5 5-5 5" fill="none" stroke="#ccc" stroke-width="1.4"/></svg></span>
  </div>
  <div class="hero__badges">
    <span class="badge-plain"></span>
    <span class="badge-cert"></span>
  </div>
</section>

<section class="services">
  <article class="service-card" style="left:60px">
    <div class="service-card__icon"><svg width="26" height="22" viewBox="0 0 26 22"><rect x="1" y="2" width="20" height="14" rx="1" fill="none" stroke="#fff" stroke-width="2"/><path d="M8 20h8M12 16v4" stroke="#fff" stroke-width="2"/><circle cx="20" cy="6" r="4" fill="#3a3a3a" stroke="#fff" stroke-width="2"/></svg></div>
    <h3 class="service-card__title">Keywords here would be Vendrik System Audit</h3>
    <p class="service-card__text">Desires to obtain pain of itself, because it is pain, but because occasionally circum-stances occur in which toil and.</p>
    <a class="btn-outline" href="#">READ MORE</a>
  </article>
  <article class="service-card" style="left:216px">
    <div class="service-card__icon service-card__icon--accent"><svg width="22" height="22" viewBox="0 0 22 22"><circle cx="11" cy="11" r="8" fill="none" stroke="#fff" stroke-width="2.4"/></svg></div>
    <h3 class="service-card__title">Vendrik Performance Optimisation</h3>
    <p class="service-card__text">pleasure and praising pain was born and I will give you a complete account of the system, and expound the actual.</p>
    <a class="btn-outline btn-outline--accent" href="#">READ MORE</a>
  </article>
  <article class="service-card" style="left:370px">
    <div class="service-card__icon"><svg width="26" height="22" viewBox="0 0 26 22"><path d="M8 9a5 5 0 0 1 10-1 4 4 0 0 1 0 7H8a3 3 0 0 1 0-6z" fill="none" stroke="#fff" stroke-width="1.8"/><rect x="2" y="16" width="22" height="5" rx="2" fill="#fff"/></svg></div>
    <h3 class="service-card__title">Vendrik Website Emergency Recovery</h3>
    <p class="service-card__text">Desires to obtain pain of itself, because it is pain, but because occasionally circum-stances occur in which toil and.</p>
    <a class="btn-outline" href="#">READ MORE</a>
  </article>
  <article class="service-card" style="left:525px">
    <div class="service-card__icon"><svg width="24" height="24" viewBox="0 0 24 24"><ellipse cx="10" cy="5" rx="8" ry="3" fill="#fff"/><path d="M2 9c0 2 16 2 16 0M2 14c0 2 10 2 12 1" stroke="#fff" stroke-width="2.4" fill="none"/><path d="M18 14v8M14 18h8" stroke="#fff" stroke-width="2.4"/></svg></div>
    <h3 class="service-card__title">Vendrik Development Infrastructure Hosting</h3>
    <p class="service-card__text">pleasure and praising pain was born and I will give you a complete account of the system, and expound the actual.</p>
    <a class="btn-outline" href="#">READ MORE</a>
  </article>
</section>

<section class="intro-cols">
  <div class="intro-col" style="left:60px">
    <h2>Why<br>Tralvo?</h2>
    <p>Fast Vendrik-based online stores, built on time and to specification, backed by effective, focused support, means that our clients are among the happiest in the eCommerce world.</p>
    <a class="text-link" href="#">Contact Us Now!</a>
  </div>
  <div class="intro-col" style="left:278px">
    <h2>Why<br>Vendrik?</h2>
    <p>Vendrik is the world's leading open source eCommerce platform. No other open-source or free system offers out-of-the-box functionality and search engine friendli-ness comparable to Vendrik CE.</p>
    <a class="text-link" href="#">Read More about Vendrik &amp; Tralvo</a>
  </div>
  <div class="intro-col" style="left:496px">
    <h2>What<br>We Do.</h2>
    <p>From support, maintenance and upgrades to redesigns, migrations and full site builds, we make your online store do what you need it to do.</p>
    <a class="text-link" href="#">Read More</a>
  </div>
</section>

<section class="cert-band">
  <div class="cert-band__badge"></div>
  <h3>VENDRIK CERTIFIED DEVELOPER</h3>
  <p>Mistaken idea of denouncing pleasure and praising pain was born and I will give you a complete account of the system, and expound the actual teachings of the great explorer of the truth, the master-builder of human happiness. No one rejects, dislikes, or avoids pleasure itself, because it is pleasure, but because those who do not know how to pursue pleasure rationally encounter consequences that are extremely painful. Nor again is there anyone who loves or pursues or desires to obtain pain of itself, because it is pain, but because occasionally circumstances occur in which toil and pain can procure him some great pleasure. To take a trivial example, which of us ever undertakes laborious physical exercise, except to obtain some advantage from it?</p>
</section>

<footer class="site-footer">
  <div class="footer-brand"><span class="footer-brand__mark"></span><span class="footer-brand__name">Halvert</span></div>
  <div class="footer-address">
    <h4>ADDRESS</h4>
    <p>Suite 42, Level 3|8 Harlow Bend Road<br>Wendale Flats VIC 3921</p>
    <p>support@mibrel.example</p>
    <p>1300 648 507</p>
  </div>
  <div class="tech-strip">
    <span>Vendrik</span><span>DataNest</span>
    <span>QRX</span><span>KLV</span>
  </div>
  <div class="footer-map" role="img" aria-label="Grayscale street map of the office location"></div>
</footer>
<div class="footer-rule"></div>
</body>
</html>
```